KELU Nature Soap

We need to design new product Nature and medicative Soap.Made in Malaysia
* 100% natural.
* made from nature Tropic oil.
* Very effective for Acne & Skin irritation
* size 100 Gm.
* Use for all skin types including sensitive skin
* Name of the product " KELU Soap"

Reason: please I need to extended since I haven't receive any suitable design for my project

Target Market(s)

International

Industry/Entity Type

Hair And Beauty

Font styles to use
Serif

Colors
33a6d7
abd037
fbed22

Requirements
Must have
• * must have English- Arabic ingredient
• * Very effective for Acne & Skin irritation
Nice to have
• * some things related to natural (water,tree,face..)
• * Show faces picture (after - before)

```html
<!DOCTYPE html>
<html lang="en">
<head>
<meta charset="UTF-8">
<title>KELU Soap – Box Artwork</title>
<link rel="stylesheet" href="https://fonts.googleapis.com/css2?family=Roboto:ital,wght@0,300;0,400;1,400&family=Roboto+Condensed:ital,wght@0,400;0,700;1,400&family=Noto+Naskh+Arabic:wght@400;700&display=swap">
<style>
  :root {
    --canvas-bg: #eef0f3;
    --panel-front: #c6d3f4;
    --panel-side: #bdcbef;
    --ink: #1c1e28;
    --brand-blue: #1f3f9c;
  }
  * { margin: 0; padding: 0; box-sizing: border-box; }
  html, body {
    width: 1200px; height: 1200px; overflow: hidden;
    background: var(--canvas-bg);
  }
  .box-net {
    position: absolute;
    left: 115px; top: 300px;
    width: 970px; height: 600px;
    display: flex;
  }
  .panel-side {
    position: relative;
    width: 230px; height: 100%;
    background: var(--panel-side);
  }
  .panel-front {
    position: relative;
    width: 740px; height: 100%;
    background: var(--panel-front);
    color: var(--ink);
  }
  .ingredients {
    position: absolute;
    left: 22px; top: 165px; width: 185px;
    font-family: "Roboto Condensed", sans-serif;
    font-size: 12.5px; line-height: 1.3;
    color: var(--ink);
  }
  .ingredients p { margin-bottom: 14px; }
  .ingredients p.narrow { width: 88px; }
  .ingredients .label { font-weight: 700; }
  .ingredients p.arabic {
    font-family: "Noto Naskh Arabic", serif;
    font-size: 13px; line-height: 1.45;
    direction: rtl; text-align: right;
  }
  .vine-art {
    position: absolute; left: 0; top: 0;
    width: 505px; height: 430px;
    clip-path: polygon(0 0, 505px 0, 505px 200px, 440px 330px, 330px 430px, 250px 400px, 218px 300px, 218px 150px, 60px 110px, 0 40px);
    background:
      radial-gradient(circle at 60% 30%, rgba(244,207,58,0.45), transparent 45%),
      radial-gradient(circle at 40% 60%, rgba(143,191,154,0.55), transparent 55%),
      linear-gradient(160deg, #b9d0c8, #c9d3ea);
    z-index: 2;
  }
  .brand-mark {
    position: absolute; left: 530px; top: 70px; width: 120px;
    display: flex; flex-direction: column; align-items: center; gap: 14px;
  }
  .brand-mark .dot {
    width: 86px; height: 86px; border-radius: 50%;
    background: var(--brand-blue);
  }
  .brand-mark .name {
    font-family: "Roboto", sans-serif; font-weight: 400;
    font-size: 30px; letter-spacing: 2px; color: var(--brand-blue);
  }
  .product-name {
    position: absolute; right: 52px; top: 300px;
    font-family: "Roboto", sans-serif; font-weight: 300;
    font-size: 88px; letter-spacing: -2px; line-height: 1;
  }
  .tagline {
    position: absolute; right: 52px; top: 425px;
    font-family: "Roboto Condensed", sans-serif; font-style: italic;
    font-size: 14px;
  }
  .skin-types {
    position: absolute; right: 52px; top: 462px;
    font-family: "Roboto Condensed", sans-serif;
    font-size: 19px;
  }
  .weight {
    position: absolute; right: 52px; top: 518px;
    font-family: "Roboto", sans-serif; font-weight: 300;
    font-size: 46px; line-height: 1;
  }
  .natural-claim {
    position: absolute; left: 52px; top: 462px;
    font-family: "Roboto", sans-serif; font-weight: 300;
    font-size: 47px; line-height: 1;
  }
  .efficacy-badge {
    position: absolute; left: 56px; top: 522px;
    padding: 7px 12px;
    border: 1.5px solid var(--ink);
    font-family: "Roboto Condensed", sans-serif;
    font-size: 22px; line-height: 1.2;
  }
  .efficacy-badge strong { font-weight: 700; }
</style>
</head>
<body>
  <div class="box-net">
    <section class="panel-side">
      <div class="ingredients">
        <p class="narrow" lang="en"><span class="label">Ingredients:</span> tropic palm oil, coconut oil, water, glycerin, neem leaf extract, aloe vera, tea tree oil.</p>
        <p class="arabic" lang="ar"><span class="label">المكونات:</span> زيت النخيل الاستوائي، زيت جوز الهند، ماء، جلسرين، خلاصة أوراق النيم، الصبار، زيت شجرة الشاي.</p>
        <p lang="en">Wet the bar, work into a rich lather and massage over skin. Rinse well with water. Store dry.</p>
      </div>
    </section>
    <section class="panel-front">
      <div class="brand-mark">
        <span class="dot"></span>
        <span class="name">KELU</span>
      </div>
      <h1 class="product-name">KELU Soap</h1>
      <p class="tagline">Made from Nature Tropic Oil</p>
      <p class="skin-types">For all skin types including sensitive skin</p>
      <p class="weight">100 Gm</p>
      <p class="natural-claim">100% natural</p>
      <p class="efficacy-badge">Effective for <strong>Acne</strong> &amp; <strong>Skin Irritation</strong></p>
    </section>
    <div class="vine-art" role="img" aria-label="Line illustration of a branching vine with green leaves and small yellow flowers"></div>
  </div>
</body>
</html>
```